Business Card for Brevikpartners

Need to design a business card with attached logo

Target Market(s)

I'm a financial/Investment adviser so card must be professional

Industry/Entity Type

Business

Font styles to use
Serif
Sans Serif

Requirements
Must have
• Would like in include the GOLD version of my logo if possible

Teddy Brevik
President

Address is
4817 Pellingham Blvd
Dellwood, Ca. 94619

Phone
510-374-9182
Fax
925-463-7208

Email
teddy@brevikpartners.example

I also need the following tag line at the bottom of card:

Investment Advisor Representative of and Securities offered
through Harborview Capital Securities, LLC Member QMTRA, DEWB
and Registered Investment Advisor.

Nice to have
• Split color in order to incorporate GOLD LOGO
Should not have

```html
<!DOCTYPE html>
<html lang="en">
<head>
<meta charset="utf-8">
<title>Brevik Partners – Business Card</title>
<link rel="stylesheet" href="https://fonts.googleapis.com/css2?family=Arimo:wght@400&family=EB+Garamond:ital,wght@0,400;1,400;1,600&display=swap">
<style>
  :root {
    --page: #ffffff;
    --card-center: #ffffff;
    --card-edge: #c9d3d8;
    --ink: #1a1a1a;
    --gold: #c2a66a;
    --gold-light: #dcc48f;
    --band: #232323;
    --band-text: #ffffff;
  }
  * { margin: 0; padding: 0; box-sizing: border-box; }
  html, body {
    width: 1200px;
    height: 1000px;
    overflow: hidden;
    background: var(--page);
  }
  .business-card {
    position: absolute;
    left: 226px;
    top: 279px;
    width: 767px;
    height: 438px;
    overflow: hidden;
    background: radial-gradient(ellipse 62% 78% at 55% 45%, var(--card-center) 70%, var(--card-edge) 100%);
    box-shadow: 3px 4px 6px rgba(0, 0, 0, 0.18);
  }
  .brand {
    position: absolute;
    left: 470px;
    top: 30px;
    width: 274px;
    text-align: center;
  }
  .brand-dot {
    display: block;
    width: 96px;
    height: 96px;
    margin: 0 auto 16px;
    border-radius: 50%;
    background: var(--gold);
  }
  .brand-name {
    font-family: "EB Garamond", Georgia, serif;
    font-style: normal;
    font-weight: 400;
    font-size: 28px;
    letter-spacing: 1.5px;
    color: var(--gold);
    white-space: nowrap;
  }
  .contact {
    position: absolute;
    left: 64px;
    top: 174px;
    color: var(--ink);
  }
  .contact-name {
    font-family: "Arimo", Arial, sans-serif;
    font-weight: 400;
    font-size: 22px;
    line-height: 26px;
  }
  .contact-title {
    font-family: "EB Garamond", Georgia, serif;
    font-style: italic;
    font-size: 16px;
    line-height: 20px;
  }
  .contact-address {
    margin-top: 28px;
    font-family: "Arimo", Arial, sans-serif;
    font-style: normal;
    font-size: 12px;
    line-height: 15px;
  }
  .contact-lines {
    margin-top: 8px;
    font-family: "Arimo", Arial, sans-serif;
    font-size: 12px;
    line-height: 15px;
  }
  .contact-label {
    font-family: "EB Garamond", Georgia, serif;
    font-style: italic;
    font-weight: 600;
    font-size: 12px;
  }
  .contact-email {
    margin-top: 13px;
    font-family: "Arimo", Arial, sans-serif;
    font-size: 15px;
    line-height: 18px;
  }
  .gold-rule {
    position: absolute;
    left: 0;
    top: 366px;
    width: 100%;
    height: 3px;
    background: linear-gradient(90deg, var(--gold), var(--gold-light) 50%, var(--gold));
  }
  .disclosure-band {
    position: absolute;
    left: 0;
    top: 369px;
    width: 100%;
    height: 69px;
    background: var(--band);
    display: flex;
    align-items: center;
    justify-content: center;
  }
  .disclosure {
    font-family: "EB Garamond", Georgia, serif;
    font-style: italic;
    font-size: 15px;
    line-height: 19px;
    color: var(--band-text);
    text-align: center;
  }
</style>
</head>
<body>
  <section class="business-card">
    <div class="brand">
      <span class="brand-dot"></span>
      <div class="brand-name">Brevik Partners</div>
    </div>

    <div class="contact">
      <h1 class="contact-name">Teddy Brevik</h1>
      <p class="contact-title">President</p>
      <address class="contact-address">
        4817 Pellingham Blvd.<br>
        Dellwood, Ca. 94619
      </address>
      <p class="contact-lines">
        <span class="contact-label">Phone:</span> 510.374.9182<br>
        <span class="contact-label">Fax:</span> 925.463.7208
      </p>
      <p class="contact-email">teddy@brevikpartners.example</p>
    </div>

    <div class="gold-rule"></div>
    <footer class="disclosure-band">
      <p class="disclosure">
        Investment Advisor Representative of and Securities offered through Harborview Capital Securities,<br>
        LLC Member QMTRA, DEWB and Registered Investment Advisor.
      </p>
    </footer>
  </section>
</body>
</html>
```